【依頼の目的/概要】
電子書籍(pavlo)の表紙デザインをお願いします

【画像サイズ】
*RVSより抜粋
表紙ファイルの理想的な寸法は2,560×1,600ピクセルです。
注:画像の寸法は1,000×625ピクセル以上であることが必要です
画像の最大の寸法は10,000×10,000ピクセルです

【タイトル】
朝の庭で見つけた小さな灯りの話

サブキャッチ
~来場者2倍、満足度9割の老舗書店を育てた5つの習慣

【著者】
ミドリノタネ工房代表
組織進化コンサルタント
柳瀬 公平

【本の内容】
とても勤勉で勉強家の開業歯科医のみなさんが
がんばってもなかなか成果の出づらい分野、
「チーム創り」について。

まず互いを人として大事にすることで
スタッフが自然に結束し、
「ここで働けてよかった」
と思うようになる。
楽しいから自主的創造的に動くようになる。
すると成果の質も高くなる。
そうなるまでのステップを紹介。

著者はレポートを出す型のコンサルではなく、
現場に入り込んでゲーム性の高い体験型研修や
一人一人の話を聴いて言葉にならない本音を通訳することなどが得意。
愛と遊び心をもってプログラムを提供し伴走するので
笑顔が絶えることがない。

*参考資料として原稿を添付します

【デザイン要望】
特にイメージにこだわりはありませんので
自由な発想でのデザインご応募を楽しみにしています。

*次点、次々点の方への参加報酬を設定いたしました。

*その他、必要な情報がありましたらお問い合わせください。

スマホでpavloを見るとき、小さなアイコンが並ぶ中で最も目に留まるデザインで、
一目で重要なワードも目に入るデザインだったので採用させていただきました。

次点の二つについても同様の基準でしたが
色使いやフォントサイズなどを調整して、
もっとパッと目に入るものでしたら順序が変わったかもしれません。

特に、チームがテーマなので人の写真+見やすいデザインが両方だったらよりよかったかなと思います

皆さま、一所懸命やっていただいてありがとうございました。
こんなにもたくさんの方にご提案いただけてとてもうれしいです。
お礼を出せるのは3作品ですが
皆様にお礼を改めて申し上げたいと思います。

電子書籍の売れ行きにとても大事な表紙づくりのご協力、本当にありがとうございました。

```html
<!DOCTYPE html>
<html lang="ja">
<head>
<meta charset="UTF-8">
<title>朝の庭で見つけた小さな灯りの話</title>
<link href="https://fonts.googleapis.com/css2?family=Noto+Sans+JP:wght@500;700;900&display=swap" rel="stylesheet">
<style>
  :root {
    --sky: #4db2e6;
    --navy: #17315f;
    --white: #ffffff;
    --yellow: #f3e83a;
    --gold: #f5d21c;
    --accent-blue: #1f7fc4;
  }
  html, body { margin: 0; padding: 0; overflow: hidden; }
  body { width: 750px; height: 1200px; font-family: "Noto Sans JP", sans-serif; }
  .cover {
    position: relative;
    width: 750px;
    height: 1200px;
    background: var(--sky);
    overflow: hidden;
  }
  .cover-graphics { position: absolute; inset: 0; }
  .title {
    position: absolute;
    top: 110px;
    left: 0;
    width: 750px;
    margin: 0;
    text-align: center;
    font-weight: 900;
    line-height: 1.08;
    transform: skewX(-4deg);
  }
  .title > span { display: block; }
  .title-line-1 { font-size: 92px; color: var(--navy); letter-spacing: 2px; }
  .title-line-2 { font-size: 76px; color: var(--navy); letter-spacing: 1px; margin-top: 6px; }
  .title-line-3 { font-size: 116px; color: var(--white); letter-spacing: 4px; margin-top: 8px; }
  .author {
    position: absolute;
    top: 618px;
    left: 0;
    width: 750px;
    display: flex;
    justify-content: center;
    align-items: center;
    gap: 14px;
    color: var(--navy);
  }
  .author-tag {
    background: var(--navy);
    color: var(--white);
    font-size: 16px;
    font-weight: 700;
    padding: 4px 6px;
    line-height: 1.1;
  }
  .author-roles { font-size: 15px; font-weight: 700; line-height: 1.45; }
  .author-name { font-size: 36px; font-weight: 900; letter-spacing: 4px; margin-left: 10px; }
  .tagline {
    position: absolute;
    top: 922px;
    left: 0;
    width: 750px;
    margin: 0;
    text-align: center;
    color: var(--navy);
    font-weight: 900;
    line-height: 1.15;
    white-space: nowrap;
  }
  .tagline > .tagline-line { display: block; }
  .tagline-line-1 { font-size: 40px; }
  .tagline-line-2 { font-size: 48px; margin-top: 6px; }
  .tagline-line-3 { font-size: 84px; margin-top: 8px; letter-spacing: 2px; }
  .tagline .figure { display: inline; font-size: 1.4em; line-height: 1; }
  .tagline-line-3 .figure { font-size: 1.15em; }
  .tagline .highlight { display: inline; color: var(--accent-blue); }
</style>
</head>
<body>
<main class="cover">
  <svg class="cover-graphics" width="750" height="1200" viewBox="0 0 750 1200" aria-hidden="true">
    <g class="rays" stroke="#ffffff" stroke-width="5" stroke-linecap="round" opacity="0.9">
      <line x1="90" y1="90" x2="150" y2="150"/>
      <line x1="60" y1="200" x2="130" y2="225"/>
      <line x1="200" y1="50" x2="230" y2="110"/>
      <line x1="660" y1="90" x2="600" y2="150"/>
      <line x1="690" y1="200" x2="620" y2="225"/>
      <line x1="550" y1="50" x2="520" y2="110"/>
      <line x1="60" y1="560" x2="130" y2="535"/>
      <line x1="100" y1="660" x2="160" y2="610"/>
      <line x1="690" y1="560" x2="620" y2="535"/>
      <line x1="650" y1="660" x2="590" y2="610"/>
    </g>
    <path class="title-frame" fill="none" stroke="#f3e83a" stroke-width="5"
      d="M375 70 C520 60 640 110 630 250 C620 330 690 400 660 500 C630 620 520 700 380 690 C240 700 110 640 95 520 C80 420 140 360 120 270 C100 140 230 80 375 70 Z"/>
    <path class="tagline-band" fill="#ffffff"
      d="M0 880 C120 845 240 850 375 870 C510 890 630 845 750 860 L750 1200 L0 1200 Z"/>
    <g class="sparkles" fill="#f5d21c">
      <path d="M70 830 l8 24 l24 8 l-24 8 l-8 24 l-8 -24 l-24 -8 l24 -8 z"/>
      <path d="M150 790 l5 15 l15 5 l-15 5 l-5 15 l-5 -15 l-15 -5 l15 -5 z"/>
      <path d="M680 820 l9 26 l26 9 l-26 9 l-9 26 l-9 -26 l-26 -9 l26 -9 z"/>
      <path d="M600 800 l5 14 l14 5 l-14 5 l-5 14 l-5 -14 l-14 -5 l14 -5 z"/>
      <path d="M40 1070 l9 26 l26 9 l-26 9 l-9 26 l-9 -26 l-26 -9 l26 -9 z"/>
      <path d="M705 1060 l7 20 l20 7 l-20 7 l-7 20 l-7 -20 l-20 -7 l20 -7 z"/>
    </g>
  </svg>

  <h1 class="title">
    <span class="title-line-1">朝の庭で</span>
    <span class="title-line-2">見つけた小さな</span>
    <span class="title-line-3">灯りの話</span>
  </h1>

  <div class="author">
    <div class="author-tag">著<br>者</div>
    <div class="author-roles">ミドリノタネ工房代表<br>組織進化コンサルタント</div>
    <div class="author-name">柳瀬 公平</div>
  </div>

  <p class="tagline">
    <span class="tagline-line tagline-line-1">来場者<span class="figure">2</span>倍、満足度<span class="figure">9</span>割の</span>
    <span class="tagline-line tagline-line-2"><span class="highlight">老舗書店</span>を育てた</span>
    <span class="tagline-line tagline-line-3"><span class="figure">5</span>つの習慣</span>
  </p>
</main>
</body>
</html>
```